Signage Design Project

We are a company that sells roses at university and college graduations. We are looking for a sign for conferences. The sign will be a long lengthwise sign, 33.5w x 80xh
It doesn't need to be overwhelmingly flashy, it just needs to get our message across. We will require two signs, one with the "Tidewater Flowers" logo, and a second with the "Brightmoor Flowers" logo. These logos are uploaded in both PNG and JPEG formats. The alternative option is to create one image with both logos, but we would much prefer two separate ones. We will NOT look at anything overly flashy. Ideally we need a simple, aesthetically pleasing graphic that will look good on a vertical pop up stand.

University

• Our logo (Tidewater Flowers for one, Brightmoor Flowers for the other)

```html
<!DOCTYPE html>
<html lang="en">
<head>
<meta charset="utf-8">
<title>Graduation Flower Banners</title>
<link rel="stylesheet" href="https://fonts.googleapis.com/css2?family=Oswald:wght@500&family=Dancing+Script:wght@400&display=swap">
<style>
  :root {
    --gap-white: #ffffff;
    --sage-centre: #e2ebdb;
    --sage-edge: #bdd5b3;
    --lime-centre: #e8edd5;
    --lime-edge: #cfdaa2;
    --brand-green: #6e9a3c;
    --script-green: #6a9642;
    --ornament-core: rgba(250, 252, 244, 0.78);
    --ornament-mid: rgba(248, 251, 240, 0.45);
  }
  * { margin: 0; padding: 0; box-sizing: border-box; }
  html, body {
    width: 1034px;
    height: 1200px;
    overflow: hidden;
    background: var(--gap-white);
  }
  .banner-set {
    position: relative;
    width: 1034px;
    height: 1200px;
  }
  .banner {
    position: absolute;
    top: 0;
    height: 1200px;
    overflow: hidden;
  }
  .banner--tidewater {
    left: 0;
    width: 506px;
    background: radial-gradient(ellipse 80% 45% at 50% 55%, var(--sage-centre) 0%, var(--sage-edge) 100%);
  }
  .banner--brightmoor {
    left: 529px;
    width: 505px;
    background: radial-gradient(ellipse 80% 45% at 50% 45%, var(--lime-centre) 0%, var(--lime-edge) 100%);
  }

  /* flourish areas */
  .ornament {
    position: absolute;
    background: radial-gradient(ellipse 50% 50% at 50% 50%, var(--ornament-core) 0%, var(--ornament-mid) 45%, rgba(255,255,255,0) 100%);
  }
  .banner--tidewater .ornament--top { left: -10px; top: 20px; width: 500px; height: 300px; }
  .banner--tidewater .ornament--bottom { left: 20px; top: 870px; width: 500px; height: 310px; }
  .banner--brightmoor .ornament--top { left: -10px; top: 30px; width: 520px; height: 300px; }
  .banner--brightmoor .ornament--bottom { left: 0; top: 860px; width: 520px; height: 270px; }

  .brand-name {
    position: absolute;
    width: 431px;
    font-family: "Oswald", sans-serif;
    font-weight: 500;
    color: var(--brand-green);
    letter-spacing: -0.5px;
  }
  .brand-name span { display: block; white-space: nowrap; }
  .brand-name .brand-line-1 { text-align: center; }
  .brand-name .brand-line-2 { text-align: right; }
  .banner--tidewater .brand-name { left: 40px; top: 348px; font-size: 112px; line-height: 111px; }
  .banner--brightmoor .brand-name { left: 34px; top: 375px; font-size: 88px; line-height: 85px; }

  .brand-dot {
    display: inline-block;
    border-radius: 50%;
    background: var(--brand-green);
    vertical-align: baseline;
  }
  .banner--tidewater .brand-dot { width: 42px; height: 42px; margin-right: 16px; }
  .banner--brightmoor .brand-dot { width: 34px; height: 34px; margin-right: 14px; }

  .tagline {
    position: absolute;
    left: 0;
    right: 0;
    text-align: center;
    font-family: "Dancing Script", cursive;
    font-weight: 400;
    color: var(--script-green);
    font-size: 64px;
    line-height: 70px;
  }
  .banner--tidewater .tagline { top: 612px; }
  .banner--brightmoor .tagline { top: 600px; }
</style>
</head>
<body>
<main class="banner-set">
  <section class="banner banner--tidewater">
    <div class="ornament ornament--top" role="img" aria-label="Pale flourish of curling leaves and swirls across the top of the banner"></div>
    <div class="ornament ornament--bottom" role="img" aria-label="Pale flourish of curling leaves and swirls across the bottom of the banner"></div>
    <h1 class="brand-name"><span class="brand-line-1">Tidewater</span><span class="brand-line-2"><i class="brand-dot"></i>Flowers</span></h1>
    <p class="tagline">Flowers<br>for your<br>Graduate</p>
  </section>

  <section class="banner banner--brightmoor">
    <div class="ornament ornament--top" role="img" aria-label="Pale flourish of a leaf and sweeping strokes across the top of the banner"></div>
    <div class="ornament ornament--bottom" role="img" aria-label="Pale flourish of a leaf and sweeping strokes across the bottom of the banner"></div>
    <h1 class="brand-name"><span class="brand-line-1">Brightmoor</span><span class="brand-line-2"><i class="brand-dot"></i>Flowers</span></h1>
    <p class="tagline">Flowers<br>for your<br>Graduate</p>
  </section>
</main>
</body>
</html>
```